Promotional Double-Sided postcard

We are promoting a web cam studio (www.velmorigrove.com) and making a postcard for recruiting models. I have attached a .doc of a very basic 8.5x11 flyer we drew up which contains the same information we want conveyed in the postcard. I've also attached our website's logo.

Industry/Entity Type

Promotional

```html
<!DOCTYPE html>
<html lang="en">
<head>
<meta charset="utf-8">
<title>Velmori Grove – Model Recruiting Postcard</title>
<link href="https://fonts.googleapis.com/css2?family=Pathway+Gothic+One&family=Quicksand:wght@600;700&family=Dosis:wght@500&display=swap" rel="stylesheet">
<style>
  :root{
    --stage:#3b3b3b;
    --pink:#e0177f;
    --pink-soft:#f04a9e;
    --plum:#7c1d52;
    --plum-deep:#5e1239;
    --ink:#2a2a2a;
    --paper:#ffffff;
    --mist:#e9e9e9;
    --grey-photo-a:#8a8a8a;
    --grey-photo-b:#c4c4c4;
    --shade:rgba(40,40,40,.78);
  }
  *{margin:0;padding:0;box-sizing:border-box}
  html,body{width:1200px;height:1080px;overflow:hidden}
  body{background:var(--stage);position:relative;font-family:"Pathway Gothic One",sans-serif}

  .card{position:absolute;width:541px;height:416px;overflow:hidden}
  .card--front-a{left:49px;top:106px}
  .card--front-b{left:621px;top:106px}
  .card--front-c{left:49px;top:560px}
  .card--back{left:621px;top:560px;background:var(--paper)}

  .photo{position:absolute;inset:0}
  .photo--grey{background:linear-gradient(100deg,var(--grey-photo-b) 0%,var(--grey-photo-a) 45%,#9c9c9c 70%,#b5b5b5 100%)}
  .photo--pink{background:linear-gradient(100deg,#d45a9a 0%,#b8307a 45%,#c24488 70%,#d0609f 100%)}

  .corner-ornament{position:absolute;left:0;top:0;width:48px;height:52px;background:rgba(20,20,20,.35);border-bottom-right-radius:40px}
  .corner-splash{position:absolute;right:0;bottom:0;width:36px;height:18px;background:rgba(20,20,20,.35);border-top-left-radius:14px}

  .side-panel{position:absolute;left:46px;top:0;width:181px;height:100%;text-align:center}
  .side-panel--light{background:rgba(236,236,236,.9)}
  .side-panel--plum{background:rgba(110,20,68,.82)}

  .brand{position:absolute;left:0;right:0;top:44px;display:flex;align-items:center;justify-content:center;gap:7px;font-family:"Pathway Gothic One",sans-serif;font-size:21px;letter-spacing:.5px}
  .brand__dot{width:12px;height:12px;border-radius:50%;background:currentColor}
  .brand--pink{color:var(--pink)}
  .brand--soft{color:var(--pink-soft)}
  .brand--white{color:#fff}

  .rule{position:absolute;left:15px;right:15px;height:1px}
  .rule--pink{background:var(--pink)}
  .rule--soft{background:rgba(255,255,255,.35)}

  .badge{position:absolute;border-radius:50%;background:var(--pink);box-shadow:0 0 0 5px rgba(224,23,127,.45);display:flex;flex-direction:column;align-items:center;justify-content:center;color:#fff;font-family:"Quicksand",sans-serif;font-weight:700;line-height:1.15}
  .badge__amount{font-size:16px}
  .badge__label{font-size:11px}
  .badge--small{width:112px;height:112px;left:35px;top:148px}
  .badge--large{width:150px;height:150px;left:109px;top:199px}
  .badge--large .badge__amount{font-size:21px}
  .badge--large .badge__label{font-size:15px}

  .pitch{position:absolute;left:19px;width:145px;top:276px;font-size:11px;line-height:13.8px;text-align:center}
  .pitch--dark{color:var(--ink)}
  .pitch--light{color:#fff}

  .site{position:absolute;left:0;right:0;top:390px;font-family:"Dosis",sans-serif;font-size:12px;letter-spacing:1px}
  .site--pink{color:var(--pink)}
  .site--white{color:#fff}

  .callout{position:absolute;left:243px;top:343px;width:284px;height:47px;background:var(--shade);color:#fff;font-size:13.5px;line-height:17px;padding:5px 10px;text-transform:uppercase}
  .callout--plum{background:rgba(94,18,57,.85)}

  .brand-top-right{position:absolute;right:20px;top:58px;left:auto}

  .info-band{position:absolute;left:184px;right:0;top:217px;height:112px;background:var(--shade);color:#fff;font-size:13.5px;line-height:17.5px;padding:22px 13px 0 91px;text-align:justify}
  .footer-band{position:absolute;left:10px;right:12px;top:376px;height:28px;background:rgba(230,230,230,.6);color:var(--pink);font-size:13px;line-height:28px;text-align:center;text-transform:uppercase}

  .back-copy{position:absolute;left:20px;width:230px;text-align:center}
  .back-headline{top:46px;color:var(--pink);font-family:"Dosis",sans-serif;font-weight:500;font-size:16px;line-height:21px}
  .perks{top:148px;list-style:none;color:var(--ink);font-size:12.5px;line-height:16px}
  .perks li{margin-bottom:5px}
  .back-brand{position:absolute;left:20px;width:230px;top:310px;display:flex;justify-content:center;align-items:center;gap:7px;color:var(--pink);font-size:19px}
  .back-contact{top:363px;color:var(--ink);font-size:12.5px;line-height:16px}
  .back-contact a{color:var(--pink);text-decoration:none}
  .divider{position:absolute;left:268px;top:58px;width:1px;height:325px;background:var(--pink)}
</style>
</head>
<body>

<!-- Front, grey with side panel -->
<section class="card card--front-a">
  <div class="photo photo--grey" role="img" aria-label="Black and white photo of a young woman with long dark hair leaning on a railing"></div>
  <div class="corner-ornament" role="img" aria-label="Swirl ornament"></div>
  <div class="corner-splash" role="img" aria-label="Ink splash"></div>
  <div class="side-panel side-panel--light">
    <div class="brand brand--pink"><span class="brand__dot"></span>Velmori Grove</div>
    <div class="rule rule--pink" style="top:118px"></div>
    <div class="badge badge--small"><span class="badge__amount">$3000</span><span class="badge__label">EVERY</span><span class="badge__label">MONTH</span></div>
    <p class="pitch pitch--dark">That is a realistic number you can earn average working part-time as a live webcam model. Some full time models make that much in a WEEK, but think of what you could do with just an extra $3000 a month!</p>
    <div class="rule rule--pink" style="top:382px"></div>
    <div class="site site--pink">www.velmorigrove.com</div>
  </div>
  <p class="callout">If you've been given this flyer, it's because you could be making great money as a live webcam model.</p>
</section>

<!-- Front, grey full bleed -->
<section class="card card--front-b">
  <div class="photo photo--grey" role="img" aria-label="Black and white photo of a young woman with long dark hair leaning on a railing"></div>
  <div class="corner-ornament" role="img" aria-label="Swirl ornament"></div>
  <div class="corner-splash" role="img" aria-label="Ink splash"></div>
  <div class="brand brand--white brand-top-right"><span class="brand__dot"></span>Velmori Grove</div>
  <p class="info-band">That is a realistic number you can earn average working part-time as a live webcam model. Some full time models make that much in a WEEK, but think of what you could do with just an extra $3000 a month!</p>
  <div class="badge badge--large" style="left:109px;top:199px"><span class="badge__amount">$3000</span><span class="badge__label">EVERY</span><span class="badge__label">MONTH</span></div>
  <p class="footer-band">If you've been given this flyer, it's because you could be making great money as a live webcam model.</p>
</section>

<!-- Front, pink -->
<section class="card card--front-c">
  <div class="photo photo--pink" role="img" aria-label="Pink toned photo of a young woman with long dark hair leaning on a railing"></div>
  <div class="corner-ornament" role="img" aria-label="Swirl ornament"></div>
  <div class="corner-splash" role="img" aria-label="Ink splash"></div>
  <div class="side-panel side-panel--plum">
    <div class="brand brand--soft"><span class="brand__dot"></span>Velmori Grove</div>
    <div class="rule rule--soft" style="top:118px"></div>
    <div class="badge badge--small"><span class="badge__amount">$3000</span><span class="badge__label">EVERY</span><span class="badge__label">MONTH</span></div>
    <p class="pitch pitch--light">That is a realistic number you can earn average working part-time as a live webcam model. Some full time models make that much in a WEEK, but think of what you could do with just an extra $3000 a month!</p>
    <div class="rule rule--soft" style="top:382px"></div>
    <div class="site site--white">www.velmorigrove.com</div>
  </div>
  <p class="callout callout--plum">If you've been given this flyer, it's because you could be making great money as a live webcam model.</p>
</section>

<!-- Back -->
<section class="card card--back">
  <p class="back-copy back-headline">From the comfort of your home or in our Beverly Hills cam studio, we will help you discover one of the most lucrative yet flexible jobs there is.</p>
  <ul class="back-copy perks">
    <li>* Free photo shoots for all models. *</li>
    <li>* Artistic freedom. Nudity is entirely up to you.*</li>
    <li>* Block anyone in Los Angeles from ever seeing you online. *</li>
    <li>* Friendly staff with studio access available 24 hours a day, 7 days a week*</li>
  </ul>
  <div class="back-brand"><span class="brand__dot"></span>Velmori Grove</div>
  <p class="back-copy back-contact">Visit our website at <a href="#">www.velmorigrove.com</a><br>to contact us with any questions.</p>
  <div class="divider"></div>
</section>

</body>
</html>
```